School District In Need of Powerful Presentation

Create a modern PPT design template -- standard and widescreen -- for the Pell RU-8K school district inspired by its logo. The presentation should be a modern projection of 21st education that excites the people who view it. The school district is located in a rural farming community with a view of the rocky mountains to its west (check out this picture www.campsiteatmarblefork.example/AnimatedImages/HomeGallery/000MountainScene.jpg). People in this community want quality education for their children with opportunities for them to be successful after they graduate.

Target Market(s)

The Harbrook and Denning communities in Northern Colorado

Industry/Entity Type

Education

Font styles to use
Sans Serif

Colors
ec1f27
3176b5
acd036
fece3e
f78f20

Requirements
Must have
• The name of the school district:
• Pell County School District RU-8K Harbrook-Denning
• Website address: www.pellru8k.example/
• Email: listen@pellru8k.example
Nice to have
• A couple of color options including their current color scheme: red, gold, black
• Placeholder for pictures of students and teachers
Should not have
• Please do not use the full logo in it's current for, but you may use elements of the logo.

```html
<!DOCTYPE html>
<html lang="en">
<head>
<meta charset="utf-8">
<title>Design Idea 01b – Individual Slides</title>
<link href="https://fonts.googleapis.com/css2?family=Roboto+Condensed:wght@700&family=Roboto:wght@400;500;700&display=swap" rel="stylesheet">
<style>
  :root{
    --red:#ec1f27; --blue:#3176b5; --green:#acd036; --gold:#fece3e; --orange:#f78f20;
    --maroon:#8d0a0e; --ink:#222; --muted:#9a9a9a; --page:#000;
  }
  html,body{margin:0;width:1200px;height:1200px;overflow:hidden;background:var(--page);}
  body{position:relative;font-family:"Roboto",sans-serif;}
  .sheet-title{position:absolute;top:14px;left:0;width:1200px;text-align:center;margin:0;
    font:700 50px/1 "Roboto Condensed",sans-serif;color:#3b3b3b;letter-spacing:1px;}
  .sheet-sub{position:absolute;top:82px;left:0;width:1200px;text-align:center;margin:0;
    font:700 29px/1 "Roboto Condensed",sans-serif;color:#555;}
  .slide{position:absolute;width:560px;height:315px;display:block;}
  .s1{left:22px;top:186px}.s2{left:614px;top:186px}
  .s3{left:22px;top:517px}.s4{left:614px;top:517px}
  .s5{left:22px;top:847px}.s6{left:616px;top:847px}
  svg text{font-family:"Roboto",sans-serif;}
  .hd{font:700 19px "Roboto",sans-serif;fill:#fff;text-anchor:middle;}
  .foot{font-size:7.2px;font-weight:700;fill:#111;}
  .small{font-size:6px;fill:#777;}
  .tiny{font-size:5px;fill:#aaa;}
  .lbl{font-size:9px;fill:#444;}
  .b9{font-size:9px;font-weight:500;fill:#333;}
  .it{font-size:6px;font-style:italic;fill:#555;}
  .wt{fill:#fff;text-anchor:middle;}
</style>
</head>
<body>
<h1 class="sheet-title">DESIGN IDEA - 01b</h1>
<p class="sheet-sub">Individual Slides</p>

<svg width="0" height="0" style="position:absolute">
  <defs>
    <linearGradient id="hdr" x1="0" x2="1"><stop offset="0" stop-color="#b01016"/><stop offset="1" stop-color="#5a0306"/></linearGradient>
    <linearGradient id="mtn" x1="0" x2="0" y1="0" y2="1"><stop offset="0" stop-color="#e8e8e8"/><stop offset="1" stop-color="#fafafa"/></linearGradient>
    <symbol id="chrome" viewBox="0 0 700 394">
      <rect width="700" height="394" fill="#fff"/>
      <rect x="12" y="6" width="112" height="38" fill="url(#mtn)" role="img" aria-label="Sketch of the mountain range to the west"/>
      <rect x="141" y="0" width="421" height="45" fill="url(#hdr)"/>
      <circle cx="628" cy="34" r="8" fill="var(--red)"/>
      <text x="639" y="37" font-size="9" font-weight="700" fill="#3a2a20">Pell RU-8K</text>
      <g>
        <rect x="0" y="355" width="67" height="3" fill="var(--red)"/>
        <rect x="70" y="355" width="67" height="3" fill="var(--blue)"/>
        <rect x="140" y="355" width="67" height="3" fill="var(--green)"/>
        <rect x="210" y="355" width="67" height="3" fill="var(--gold)"/>
        <rect x="280" y="355" width="67" height="3" fill="var(--red)"/>
        <rect x="350" y="355" width="67" height="3" fill="var(--blue)"/>
        <rect x="420" y="355" width="67" height="3" fill="var(--green)"/>
        <rect x="490" y="355" width="67" height="3" fill="var(--gold)"/>
        <rect x="560" y="355" width="67" height="3" fill="var(--red)"/>
        <rect x="630" y="355" width="70" height="3" fill="var(--orange)"/>
      </g>
      <text class="foot" x="26" y="379">Pell County School District RU-8K Harbrook-Denning</text>
      <circle cx="289" cy="376" r="9" fill="var(--orange)"/>
      <path d="M283 377 L289 371 L295 377 M285 376 V381 H293 V376" fill="none" stroke="#fff" stroke-width="1.5"/>
      <text class="foot" x="307" y="379">Website - www.pellru8k.example/</text>
      <circle cx="507" cy="376" r="9" fill="var(--orange)"/>
      <rect x="502" y="372" width="10" height="7" fill="none" stroke="#fff" stroke-width="1.2"/>
      <path d="M502 372 L507 376 L512 372" fill="none" stroke="#fff" stroke-width="1.2"/>
      <text class="foot" x="526" y="379">eMail - listen@pellru8k.example</text>
    </symbol>
  </defs>
</svg>

<!-- Slide 1: pencil steps -->
<svg class="slide s1" viewBox="0 0 700 394">
  <use href="#chrome"/>
  <text class="hd" x="351" y="32">ENTER YOUR TITLE</text>
  <g class="pencils" font-size="9">
    <g><text class="lbl" x="149" y="102" text-anchor="middle">Title-01</text><line x1="149" y1="118" x2="149" y2="163" stroke="#bbb"/><circle cx="149" cy="118" r="2.5" fill="#bbb"/>
      <polygon points="110,222 149,163 188,222" fill="#d9d9d9"/><polygon points="149,163 188,222 166,222" fill="#bdbdbd"/><polygon points="149,163 141,178 157,178" fill="#111"/>
      <rect x="110" y="222" width="78" height="91" fill="#4a7cc0"/><text class="wt" x="149" y="246" font-size="11">Step</text><text class="wt" x="149" y="272" font-size="22" font-weight="700">01</text></g>
    <g><text class="lbl" x="227" y="131" text-anchor="middle">Title-01</text><line x1="227" y1="147" x2="227" y2="163" stroke="#bbb"/><circle cx="227" cy="147" r="2.5" fill="#bbb"/>
      <polygon points="188,222 227,163 266,222" fill="#d9d9d9"/><polygon points="227,163 266,222 244,222" fill="#bdbdbd"/><polygon points="227,163 219,178 235,178" fill="#111"/>
      <rect x="188" y="222" width="78" height="91" fill="#d04343"/><text class="wt" x="227" y="246" font-size="11">Step</text><text class="wt" x="227" y="272" font-size="22" font-weight="700">02</text></g>
    <g><text class="lbl" x="305" y="102" text-anchor="middle">Title-01</text><line x1="305" y1="118" x2="305" y2="163" stroke="#bbb"/><circle cx="305" cy="118" r="2.5" fill="#bbb"/>
      <polygon points="266,222 305,163 344,222" fill="#d9d9d9"/><polygon points="305,163 344,222 322,222" fill="#bdbdbd"/><polygon points="305,163 297,178 313,178" fill="#111"/>
      <rect x="266" y="222" width="78" height="91" fill="#9bbb4d"/><text class="wt" x="305" y="246" font-size="11">Step</text><text class="wt" x="305" y="272" font-size="22" font-weight="700">03</text></g>
    <g><text class="lbl" x="383" y="131" text-anchor="middle">Title-01</text><line x1="383" y1="147" x2="383" y2="163" stroke="#bbb"/><circle cx="383" cy="147" r="2.5" fill="#bbb"/>
      <polygon points="344,222 383,163 422,222" fill="#d9d9d9"/><polygon points="383,163 422,222 400,222" fill="#bdbdbd"/><polygon points="383,163 375,178 391,178" fill="#111"/>
      <rect x="344" y="222" width="78" height="91" fill="#7e5ea6"/><text class="wt" x="383" y="246" font-size="11">Step</text><text class="wt" x="383" y="272" font-size="22" font-weight="700">04</text></g>
    <g><text class="lbl" x="461" y="102" text-anchor="middle">Title-01</text><line x1="461" y1="118" x2="461" y2="163" stroke="#bbb"/><circle cx="461" cy="118" r="2.5" fill="#bbb"/>
      <polygon points="422,222 461,163 500,222" fill="#d9d9d9"/><polygon points="461,163 500,222 478,222" fill="#bdbdbd"/><polygon points="461,163 453,178 469,178" fill="#111"/>
      <rect x="422" y="222" width="78" height="91" fill="#47acc6"/><text class="wt" x="461" y="246" font-size="11">Step</text><text class="wt" x="461" y="272" font-size="22" font-weight="700">05</text></g>
    <g><text class="lbl" x="539" y="131" text-anchor="middle">Title-01</text><line x1="539" y1="147" x2="539" y2="163" stroke="#bbb"/><circle cx="539" cy="147" r="2.5" fill="#bbb"/>
      <polygon points="500,222 539,163 578,222" fill="#d9d9d9"/><polygon points="539,163 578,222 556,222" fill="#bdbdbd"/><polygon points="539,163 531,178 547,178" fill="#111"/>
      <rect x="500" y="222" width="78" height="91" fill="#f79541"/><text class="wt" x="539" y="246" font-size="11">Step</text><text class="wt" x="539" y="272" font-size="22" font-weight="700">06</text></g>
  </g>
</svg>

<!-- Slide 2: dashboard monitors -->
<svg class="slide s2" viewBox="0 0 700 394">
  <use href="#chrome"/>
  <text class="hd" x="351" y="32">ENTER YOUR TITLE</text>
  <g class="monitors" fill="#fff" stroke="#222" stroke-width="3">
    <rect x="55" y="76" width="104" height="76"/><rect x="175" y="76" width="104" height="76"/>
    <rect x="295" y="76" width="104" height="76"/><rect x="415" y="76" width="104" height="76"/>
    <rect x="535" y="76" width="104" height="76"/>
  </g>
  <g class="charts">
    <polygon points="62,145 80,128 95,132 112,115 128,120 150,90 150,145" fill="#f79541"/>
    <polyline points="62,140 80,124 95,128 112,110 128,114 150,86" fill="none" stroke="#3176b5" stroke-width="3"/>
    <rect x="184" y="122" width="14" height="24" fill="#3176b5"/><rect x="204" y="112" width="14" height="34" fill="#d04343"/>
    <rect x="224" y="104" width="14" height="42" fill="#9bbb4d"/><rect x="244" y="128" width="14" height="18" fill="#7e5ea6"/>
    <circle cx="311" cy="96" r="8" fill="#d04343"/><circle cx="334" cy="96" r="8" fill="#9bbb4d"/><circle cx="357" cy="96" r="8" fill="#7e5ea6"/><circle cx="380" cy="96" r="8" fill="#47acc6"/>
    <g fill="#aaa"><rect x="305" y="116" width="50" height="3"/><rect x="305" y="124" width="50" height="3"/><rect x="305" y="132" width="50" height="3"/><rect x="360" y="124" width="30" height="2"/><rect x="360" y="130" width="30" height="2"/></g>
    <rect x="425" y="84" width="40" height="3" fill="#d04343"/><rect x="425" y="90" width="30" height="3" fill="#3176b5"/>
    <polyline points="425,140 445,128 465,132 485,112 505,100" fill="none" stroke="#3176b5" stroke-width="1.5"/>
    <rect x="545" y="84" width="58" height="24" fill="#cfd8e6" role="img" aria-label="World map graphic"/>
    <rect x="545" y="116" width="50" height="3" fill="#7e5ea6"/><rect x="545" y="123" width="45" height="3" fill="#47acc6"/><rect x="545" y="130" width="40" height="3" fill="#d04343"/>
    <rect x="612" y="110" width="20" height="26" fill="#ddd"/>
  </g>
  <rect x="330" y="160" width="280" height="186" rx="8" fill="#ede6dc" role="img" aria-label="Illustration of a person working at a desk in front of the monitors"/>
  <g class="notes">
    <g><rect x="55" y="202" width="4" height="4" fill="#3176b5"/><rect x="61" y="202" width="4" height="4" fill="#d04343"/><rect x="67" y="202" width="4" height="4" fill="#7e5ea6"/><rect x="73" y="202" width="4" height="4" fill="#3176b5"/><rect x="79" y="202" width="4" height="4" fill="#d04343"/><rect x="85" y="202" width="4" height="4" fill="#3176b5"/></g>
    <text class="small" x="107" y="194">Lorem ipsum dolor sit amet, consectetur</text>
    <text class="small" x="107" y="206">adipiscing elit. Sed finibus tellus varius massa</text>
    <text class="small" x="107" y="218">sagittis scelerisque. Etiam eu imperdiet felis.</text>
    <g><rect x="55" y="267" width="4" height="4" fill="#3176b5"/><rect x="61" y="267" width="4" height="4" fill="#d04343"/><rect x="67" y="267" width="4" height="4" fill="#7e5ea6"/><rect x="73" y="267" width="4" height="4" fill="#3176b5"/><rect x="79" y="267" width="4" height="4" fill="#d04343"/><rect x="85" y="267" width="4" height="4" fill="#3176b5"/></g>
    <text class="small" x="107" y="259">Lorem ipsum dolor sit amet, consectetur</text>
    <text class="small" x="107" y="271">adipiscing elit. Sed finibus tellus varius massa</text>
    <text class="small" x="107" y="283">sagittis scelerisque. Etiam eu imperdiet felis.</text>
  </g>
</svg>

<!-- Slide 3: notebook list -->
<svg class="slide s3" viewBox="0 0 700 394">
  <use href="#chrome"/>
  <text class="hd" x="351" y="32">ENTER YOUR TITLE</text>
  <rect x="4" y="66" width="254" height="290" rx="6" fill="#fff" stroke="#3a6fb5" stroke-width="4"/>
  <rect x="240" y="70" width="14" height="282" fill="#e4e4e4"/>
  <g fill="none" stroke="#555" stroke-width="2">
    <path d="M0 90 h12"/><path d="M0 107 h12"/><path d="M0 124 h12"/><path d="M0 141 h12"/><path d="M0 158 h12"/><path d="M0 175 h12"/><path d="M0 192 h12"/><path d="M0 209 h12"/><path d="M0 226 h12"/><path d="M0 243 h12"/><path d="M0 260 h12"/><path d="M0 277 h12"/><path d="M0 294 h12"/><path d="M0 311 h12"/><path d="M0 328 h12"/>
  </g>
  <g class="chapters" text-anchor="end">
    <text class="b9" x="192" y="100">Lorem Ipsum</text><text class="tiny" x="192" y="112">This Great Paragraph line is a sample lorem</text><text class="tiny" x="192" y="122">ipsum dolor</text>
    <line x1="202" y1="98" x2="232" y2="98" stroke="var(--blue)"/><circle cx="202" cy="98" r="2" fill="var(--blue)"/><polygon points="232,88 264,88 258,98 264,108 232,108" fill="var(--blue)"/>
    <text class="b9" x="192" y="146">Frontal Lobe</text><text class="tiny" x="192" y="158">This Great Paragraph line is a sample lorem</text><text class="tiny" x="192" y="168">ipsum dolor</text>
    <line x1="202" y1="144" x2="236" y2="144" stroke="var(--red)"/><circle cx="202" cy="144" r="2" fill="var(--red)"/><polygon points="236,134 268,134 262,144 268,154 236,154" fill="var(--red)"/>
    <text class="b9" x="192" y="192">Cerebelum</text><text class="tiny" x="192" y="204">This Great Paragraph line is a sample lorem</text><text class="tiny" x="192" y="214">ipsum dolor</text>
    <line x1="202" y1="190" x2="240" y2="190" stroke="var(--green)"/><circle cx="202" cy="190" r="2" fill="var(--green)"/><polygon points="240,180 272,180 266,190 272,200 240,200" fill="#8dc63f"/>
    <text class="b9" x="192" y="238">Parietal Lobe</text><text class="tiny" x="192" y="250">This Great Paragraph line is a sample lorem</text><text class="tiny" x="192" y="260">ipsum dolor</text>
    <line x1="202" y1="236" x2="244" y2="236" stroke="#7e5ea6"/><circle cx="202" cy="236" r="2" fill="#7e5ea6"/><polygon points="244,226 276,226 270,236 276,246 244,246" fill="#7e5ea6"/>
    <text class="b9" x="192" y="284">Laudantium</text><text class="tiny" x="192" y="296">This Great Paragraph line is a sample lorem</text><text class="tiny" x="192" y="306">ipsum dolor</text>
    <line x1="202" y1="282" x2="248" y2="282" stroke="#47acc6"/><circle cx="202" cy="282" r="2" fill="#47acc6"/><polygon points="248,272 280,272 274,282 280,292 248,292" fill="#47acc6"/>
    <text class="b9" x="192" y="330">Occipital Lobe</text><text class="tiny" x="192" y="342">This Great Paragraph line is a sample lorem</text><text class="tiny" x="192" y="350">ipsum dolor</text>
    <line x1="202" y1="328" x2="252" y2="328" stroke="var(--orange)"/><circle cx="202" cy="328" r="2" fill="var(--orange)"/><polygon points="252,318 284,318 278,328 284,338 252,338" fill="var(--orange)"/>
  </g>
  <g><rect x="340" y="104" width="4" height="4" fill="#3176b5"/><rect x="346" y="104" width="4" height="4" fill="#d04343"/><rect x="352" y="104" width="4" height="4" fill="#7e5ea6"/><rect x="358" y="104" width="4" height="4" fill="#3176b5"/><rect x="364" y="104" width="4" height="4" fill="#d04343"/><rect x="370" y="104" width="4" height="4" fill="#3176b5"/></g>
  <text class="small" x="391" y="96" font-size="7">Lorem ipsum dolor sit amet, consectetur adipiscing elit. Sed</text>
  <text class="small" x="391" y="109" font-size="7">finibus tellus varius massa sagittis scelerisque. Etiam eu</text>
  <text class="small" x="391" y="122" font-size="7">imperdiet felis.</text>
  <text class="small" x="316" y="151" font-size="7">Lorem Ipsum is simply dummy text of the printing and typesetting industry.</text>
  <text class="small" x="316" y="162" font-size="7">Lorem Ipsum has been the industry's standard dummy text ever since the</text>
  <text class="small" x="316" y="173" font-size="7">1500s.</text>
  <g class="bullets">
    <text class="it" x="334" y="209">➢   Lorem Ipsum is simply dummy text of the printing and typesetting industry.</text>
    <text class="it" x="334" y="230">➢   Lorem Ipsum has been the industry's standard dummy text ever since the 1500s.</text>
    <text class="it" x="334" y="251">➢   It has survived not only five centuries, but also the leap into electronic typesetting,</text>
    <text class="it" x="346" y="261">remaining essentially unchanged.</text>
    <text class="it" x="334" y="282">➢   It was popularised in the 1960s with the release of sheets containing Lorem</text>
    <text class="it" x="346" y="292">Ipsum.</text>
    <text class="it" x="334" y="313">➢   Lorem Ipsum has been the industry's standard dummy text ever since the 1500s.</text>
    <text class="it" x="334" y="334">➢   It has survived not only five centuries, but also the leap into electronic typesetting,</text>
    <text class="it" x="346" y="344">remaining essentially unchanged.</text>
  </g>
</svg>

<!-- Slide 4: graduate hub -->
<svg class="slide s4" viewBox="0 0 700 394">
  <use href="#chrome"/>
  <text class="hd" x="351" y="32">ENTER YOUR TITLE</text>
  <circle cx="351" cy="196" r="130" fill="#f3f3f3" role="img" aria-label="Faint cloud of education icons"/>
  <circle cx="351" cy="198" r="68" fill="#f4a460" stroke="#111" stroke-width="3" role="img" aria-label="Illustration of a graduate student in cap and gown"/>
  <g class="tiles">
    <rect x="202" y="108" width="48" height="48" rx="6" fill="var(--blue)"/><rect x="216" y="122" width="20" height="20" rx="2" fill="none" stroke="#fff" stroke-width="2"/>
    <rect x="434" y="108" width="48" height="48" rx="6" fill="#8dc63f"/><rect x="448" y="122" width="20" height="20" rx="2" fill="none" stroke="#fff" stroke-width="2"/>
    <rect x="202" y="233" width="48" height="48" rx="6" fill="#d04343"/><rect x="216" y="247" width="20" height="20" rx="2" fill="none" stroke="#fff" stroke-width="2"/>
    <rect x="434" y="233" width="48" height="48" rx="6" fill="#7e5ea6"/><rect x="448" y="247" width="20" height="20" rx="2" fill="none" stroke="#fff" stroke-width="2"/>
  </g>
  <g text-anchor="end">
    <text class="b9" x="186" y="121" font-weight="700">Enter Your Title</text>
    <text class="tiny" x="186" y="135">Ipsum generators on the Internet tend</text><text class="tiny" x="186" y="144">to repeat predefined chunks</text>
    <text class="b9" x="186" y="247" font-weight="700">Enter Your Title</text>
    <text class="tiny" x="186" y="264">Ipsum generators on the Internet tend</text><text class="tiny" x="186" y="273">to repeat predefined chunks</text>
  </g>
  <text class="b9" x="499" y="121" font-weight="700">Enter Your Title</text>
  <text class="tiny" x="499" y="135">Ipsum generators on the Internet tend</text><text class="tiny" x="499" y="144">to repeat predefined chunks</text>
  <text class="b9" x="496" y="247" font-weight="700">Enter Your Title</text>
  <text class="tiny" x="495" y="260">Ipsum generators on the Internet tend</text><text class="tiny" x="495" y="269">to repeat predefined chunks</text>
</svg>

<!-- Slide 5: pyramid infographic -->
<svg class="slide s5" viewBox="0 0 700 394">
  <use href="#chrome"/>
  <text class="hd" x="351" y="32">INFOGRAPGHIC STYLE TEMPLATE</text>
  <text x="40" y="91" font-size="14" font-weight="500" fill="#555">Enter Title - 01</text>
  <text class="tiny" x="40" y="105" font-size="6">Suitable for all category, Lorem Ipsum</text>
  <text class="tiny" x="40" y="114" font-size="6">is not simply random text.</text>
  <text class="tiny" x="40" y="145" font-size="6">For every 6 emails received, we get 3 Phone calls.</text>
  <text class="tiny" x="40" y="155" font-size="6">Suitable for all categories business and personal</text>
  <text class="tiny" x="40" y="165" font-size="6">presentation, Suitable for all categories business and</text>
  <text class="tiny" x="40" y="175" font-size="6">personal presentation, eaque ipsa quae ab illo</text>
  <text class="tiny" x="40" y="185" font-size="6">inventore veritatis et quasi</text>
  <text x="40" y="235" font-size="14" font-weight="500" fill="#555">Enter Title - 02</text>
  <text class="tiny" x="40" y="249" font-size="6">Suitable for all category, Lorem Ipsum</text>
  <text class="tiny" x="40" y="258" font-size="6">is not simply random text.</text>
  <g class="ribbons">
    <rect x="320" y="78" width="210" height="44" fill="#f0f0f0"/>
    <polygon points="282,78 320,78 330,122 292,122" fill="#3f6eab"/>
    <rect x="292" y="126" width="220" height="44" fill="#f0f0f0"/>
    <polygon points="254,126 292,126 302,170 264,170" fill="#b53a3a"/>
    <rect x="264" y="174" width="230" height="44" fill="#f0f0f0"/>
    <polygon points="226,174 264,174 274,218 236,218" fill="#8aab3f"/>
    <rect x="236" y="222" width="240" height="44" fill="#f0f0f0"/>
    <polygon points="198,222 236,222 246,266 208,266" fill="#6b4f92"/>
    <rect x="208" y="270" width="250" height="44" fill="#f0f0f0"/>
    <polygon points="170,270 208,270 218,314 180,314" fill="#3c9db7"/>
  </g>
  <g class="ribbon-text">
    <text class="b9" x="345" y="94">Target</text><text class="tiny" x="345" y="105">We recommend you to put a little words for this</text><text class="tiny" x="345" y="114">awesome stuff as a details.</text>
    <text class="b9" x="317" y="142">Value</text><text class="tiny" x="317" y="153">We recommend you to put a little words for this</text><text class="tiny" x="317" y="162">awesome stuff as a details.</text>
    <text class="b9" x="289" y="190">Key Objectives</text><text class="tiny" x="289" y="201">We recommend you to put a little words for this</text><text class="tiny" x="289" y="210">awesome stuff as a details.</text>
    <text class="b9" x="261" y="238">Mission</text><text class="tiny" x="261" y="249">We recommend you to put a little words for this</text><text class="tiny" x="261" y="258">awesome stuff as a details.</text>
    <text class="b9" x="233" y="286">Vision</text><text class="tiny" x="233" y="297">We recommend you to put a little words for this</text><text class="tiny" x="233" y="306">awesome stuff as a details.</text>
  </g>
  <g class="pyramid">
    <polygon points="550,70 528,118 572,118" fill="#3f6eab"/><polygon points="550,70 572,118 584,118" fill="#2d5283"/>
    <polygon points="528,118 572,118 584,118 606,166 494,166" fill="#c94040"/>
    <polygon points="494,166 606,166 628,214 472,214" fill="#8aab3f"/>
    <polygon points="472,214 628,214 650,262 450,262" fill="#7b5aa3"/>
    <polygon points="450,262 650,262 670,310 432,310" fill="#3c9db7"/>
    <polygon points="660,310 670,310 662,326" fill="#256e82"/>
    <g fill="none" stroke="#fff" stroke-width="2">
      <circle cx="550" cy="103" r="6"/><circle cx="550" cy="103" r="2"/>
      <path d="M546 132 h8 M548 132 v8 l-4 8 h12 l-4 -8 v-8"/>
      <circle cx="547" cy="186" r="4"/><path d="M550 189 l6 6"/>
      <circle cx="550" cy="236" r="5"/><path d="M550 241 v6"/>
      <path d="M538 287 q12 -10 24 0 q-12 10 -24 0z"/><circle cx="550" cy="287" r="2.5"/>
    </g>
  </g>
</svg>

<!-- Slide 6: staircase infographic -->
<svg class="slide s6" viewBox="0 0 700 394">
  <use href="#chrome"/>
  <text class="hd" x="351" y="32">INFOGRAPGHIC STYLE TEMPLATE</text>
  <rect x="156" y="92" width="76" height="132" rx="6" fill="#e2e2e2" role="img" aria-label="Silhouette of a figure climbing the steps"/>
  <g class="steps">
    <polygon points="100,226 198,226 194,232 96,232" fill="#5c8fd0"/><rect x="96" y="232" width="98" height="18" fill="#3f6eab"/><text class="wt" x="145" y="245" font-size="8">One</text>
    <polygon points="224,192 302,192 298,198 220,198" fill="#e06060"/><rect x="220" y="198" width="78" height="18" fill="#c94040"/><text class="wt" x="259" y="211" font-size="8">Two</text>
    <polygon points="298,162 400,162 396,168 294,168" fill="#a6c86a"/><rect x="294" y="168" width="102" height="18" fill="#8aab3f"/><text class="wt" x="345" y="181" font-size="8">Three</text>
    <polygon points="394,129 494,129 490,135 390,135" fill="#9b7cc0"/><rect x="390" y="135" width="100" height="18" fill="#7b5aa3"/><text class="wt" x="440" y="148" font-size="8">Four</text>
    <polygon points="490,93 590,93 586,99 486,99" fill="#67bcd2"/><rect x="486" y="99" width="100" height="18" fill="#3c9db7"/><text class="wt" x="536" y="112" font-size="8">Five</text>
  </g>
  <g class="points">
    <circle cx="112" cy="290" r="14" fill="var(--blue)"/><path d="M106 284 h12 v4 q0 6 -6 6 q-6 0 -6 -6z M112 294 v4 M108 298 h8" fill="none" stroke="#fff" stroke-width="1.5"/>
    <text class="b9" x="134" y="279" font-size="8">Your Title</text>
    <text class="tiny" x="134" y="290">Ipsum generators on</text><text class="tiny" x="134" y="298">the Internet tend to</text><text class="tiny" x="134" y="306">repeat predefined</text><text class="tiny" x="134" y="314">chunks</text>
    <circle cx="228" cy="250" r="14" fill="var(--red)"/><path d="M222 245 l6 -2 l6 2 v4 q0 6 -6 8 q-6 -2 -6 -8z" fill="#fff"/>
    <text class="b9" x="250" y="242" font-size="8">Your Title</text>
    <text class="tiny" x="250" y="253">Ipsum generators on</text><text class="tiny" x="250" y="261">the Internet tend to</text><text class="tiny" x="250" y="269">repeat predefined</text><text class="tiny" x="250" y="277">chunks</text>
    <circle cx="328" cy="213" r="14" fill="#8dc63f"/><path d="M322 219 l10 -10 l2 2 l-10 10 h-2z" fill="#fff"/>
    <text class="b9" x="350" y="206" font-size="8">Your Title</text>
    <text class="tiny" x="350" y="217">Ipsum generators on</text><text class="tiny" x="350" y="225">the Internet tend to</text><text class="tiny" x="350" y="233">repeat predefined</text><text class="tiny" x="350" y="241">chunks</text>
    <circle cx="430" cy="181" r="14" fill="#7b5aa3"/><path d="M424 176 h12 M426 176 l1 10 h6 l1 -10" fill="none" stroke="#fff" stroke-width="1.5"/>
    <text class="b9" x="452" y="174" font-size="8">Your Title</text>
    <text class="tiny" x="452" y="185">Ipsum generators on</text><text class="tiny" x="452" y="193">the Internet tend to</text><text class="tiny" x="452" y="201">repeat predefined</text><text class="tiny" x="452" y="209">chunks</text>
    <circle cx="529" cy="143" r="14" fill="#3c9db7"/><path d="M523 149 l4 -9 l9 -3 l-3 9z" fill="none" stroke="#fff" stroke-width="1.5"/>
    <text class="b9" x="551" y="136" font-size="8">Your Title</text>
    <text class="tiny" x="551" y="147">Ipsum generators on</text><text class="tiny" x="551" y="155">the Internet tend to</text><text class="tiny" x="551" y="163">repeat predefined</text><text class="tiny" x="551" y="171">chunks</text>
  </g>
</svg>
</body>
</html>
```